Real estate for sale A-frame sign

I have a vision but do not know any software tools. I need to create a real estate sign from scratch. The sign is traditionally a 4:5 ratio--more tall than wide. The text needed on the sign is Offered by Hearthline Realty, so that is not a variable. The font, font size and colors used are the variables.

The red and gold sample has the exact text needed.
Updates

The text on the sign should be like the red and gold sample I included in my brief. Unsure why some designers are putting "governed by state law" on the sign. ??? And can we elevate the font to something more sophisticated? I included both the Lantern and marlowe's logos for inspiration. The fonts used should be similar.

Target Market(s)

sophisticated homeowners

Font styles to use
Serif
Sans Serif

Colors
0455a3
cedeed
ec1f27
ffffff
fbed22
fdf9cf

Requirements
Must have
• An elevated sense of style and class. Look to Lantern real estate and marlowe's real estate for their logo and font styles.
Nice to have
• I have a need for a:

A baccarat red background and gold text
A navy blue background with light blue text
A navy blue background with pale yellow text
A deep forest green background with white text

```html
<!DOCTYPE html>
<html lang="en">
<head>
<meta charset="utf-8">
<title>For Sale Sign</title>
<link rel="stylesheet" href="https://fonts.googleapis.com/css2?family=Bebas+Neue&family=Cinzel:wght@500&family=Montserrat:wght@600;700&display=swap">
<style>
  :root {
    --page: #f4f4f2;
    --sign-blue: #0455a3;
    --border-white: #ffffff;
    --cream: #fdf9cf;
    --gold: #d8b866;
    --gold-deep: #b8923e;
    --text-white: #ffffff;
  }
  * { margin: 0; padding: 0; box-sizing: border-box; }
  html, body {
    width: 900px;
    height: 1200px;
    overflow: hidden;
    background: var(--page);
  }
  .sign {
    position: absolute;
    left: 28px;
    top: 40px;
    width: 844px;
    height: 1120px;
    background: var(--border-white);
    box-shadow: 4px 5px 8px rgba(0, 0, 0, 0.3);
  }
  .sign-face {
    position: absolute;
    left: 22px;
    top: 20px;
    width: 800px;
    height: 1077px;
    background: var(--sign-blue);
    font-family: "Montserrat", sans-serif;
    color: var(--text-white);
  }
  .brand {
    position: absolute;
    left: 0;
    right: 0;
    top: 70px;
    display: flex;
    flex-direction: column;
    align-items: center;
    gap: 36px;
  }
  .brand-mark {
    width: 150px;
    height: 150px;
    background: linear-gradient(135deg, var(--gold), var(--gold-deep));
  }
  .brand-name {
    font-family: "Cinzel", serif;
    font-weight: 500;
    font-size: 40px;
    letter-spacing: 1px;
    color: var(--gold);
    line-height: 1;
  }
  .rule {
    position: absolute;
    left: 73px;
    width: 654px;
    height: 4px;
    background: var(--cream);
  }
  .rule-top { top: 417px; }
  .rule-bottom { top: 565px; }
  .headline {
    position: absolute;
    left: 0;
    right: 0;
    top: 436px;
    text-align: center;
    font-weight: 700;
    font-size: 106px;
    line-height: 112px;
    letter-spacing: 3px;
    color: var(--cream);
  }
  .offered {
    position: absolute;
    left: 73px;
    width: 654px;
    top: 640px;
    display: flex;
    align-items: center;
    gap: 28px;
  }
  .offered-line {
    flex: 1;
    height: 3px;
    background: var(--cream);
  }
  .offered-text {
    font-family: "Bebas Neue", sans-serif;
    font-size: 90px;
    line-height: 88px;
    color: var(--cream);
  }
  .agency {
    position: absolute;
    left: 0;
    right: 0;
    top: 726px;
    text-align: center;
    font-weight: 700;
    font-size: 50px;
    line-height: 56px;
    letter-spacing: 1px;
    color: var(--cream);
  }
  .phone-band {
    position: absolute;
    left: 0;
    right: 0;
    top: 834px;
    height: 108px;
    background: var(--cream);
    display: flex;
    align-items: center;
    justify-content: center;
    gap: 22px;
    color: var(--sign-blue);
  }
  .phone-icon { width: 64px; height: 64px; }
  .phone-number {
    font-weight: 700;
    font-size: 84px;
    line-height: 1;
    letter-spacing: 2px;
  }
  .website {
    position: absolute;
    left: 0;
    right: 0;
    top: 985px;
    text-align: center;
    font-weight: 600;
    font-size: 28px;
    letter-spacing: 4px;
    color: var(--text-white);
  }
</style>
</head>
<body>
  <div class="sign">
    <div class="sign-face">
      <div class="brand">
        <div class="brand-mark"></div>
        <div class="brand-name">REAL ESTATE</div>
      </div>

      <div class="rule rule-top"></div>
      <h1 class="headline">FOR SALE</h1>
      <div class="rule rule-bottom"></div>

      <div class="offered">
        <span class="offered-line"></span>
        <span class="offered-text">OFFERED BY</span>
        <span class="offered-line"></span>
      </div>
      <p class="agency">HEARTHLINE REALTY</p>

      <div class="phone-band">
        <svg class="phone-icon" viewBox="0 0 24 24" aria-hidden="true">
          <path fill="currentColor" d="M6.6 10.8c1.4 2.8 3.8 5.1 6.6 6.6l2.2-2.2c.3-.3.7-.4 1-.2 1.1.4 2.3.6 3.6.6.6 0 1 .4 1 1V20c0 .6-.4 1-1 1C10.6 21 3 13.4 3 4c0-.6.4-1 1-1h3.5c.6 0 1 .4 1 1 0 1.3.2 2.5.6 3.6.1.3 0 .7-.2 1l-2.3 2.2z"/>
          <path fill="none" stroke="currentColor" stroke-width="1.6" stroke-linecap="round" d="M14 3.5a7 7 0 0 1 6.5 6.5M14 7a3.5 3.5 0 0 1 3 3"/>
        </svg>
        <span class="phone-number">555 014 2290</span>
      </div>

      <p class="website">www.Hearthline.com</p>
    </div>
  </div>
</body>
</html>
```